Bref créative
Powersports business card design
Clean, professional and simple
Simple
Dale Corvin
1234 NO ADDRESS
NO CITY, NO STATE 12345
dale@ridehavenpowersports.example
ridehavenpowersports.example
Needs to be clean and simple. Use some background designs maybe, but nothing too fancy or abstract.
Logo only on back of card
Maybe a little darker blue, but still a bright blue.
Glossy, blue
Glossy, red
All black

```html
<!DOCTYPE html>
<html lang="en">
<head>
<meta charset="utf-8">
<title>RideHaven Powersports — Business Cards</title>
<link href="https://fonts.googleapis.com/css2?family=Titillium+Web:wght@400;600;700&display=swap" rel="stylesheet">
<style>
  :root {
    --bg: #d9d9d9;
    --card-white: #ffffff;
    --card-white-shade: #ececec;
    --mark-grey: #e2e2e2;
    --text-grey: #6d6d6d;
    --red: #c8141b;
    --red-dark: #8e0c10;
    --red-light: #e8333a;
    --orange: #f26a1b;
    --orange-dark: #c94a0a;
    --orange-light: #ff923f;
    --blue: #1e8fd0;
    --blue-dark: #0f5f97;
    --blue-light: #3cb0ea;
    --card-w: 320px;
    --card-h: 183px;
  }
  * { box-sizing: border-box; margin: 0; padding: 0; }
  html, body {
    width: 1200px; height: 871px; overflow: hidden;
    background: var(--bg);
    font-family: "Titillium Web", sans-serif;
  }
  .card-sheet {
    width: 1200px; height: 871px;
    display: grid;
    grid-template-columns: repeat(3, var(--card-w));
    grid-template-rows: repeat(2, var(--card-h));
    column-gap: 70px; row-gap: 120px;
    justify-content: center; align-content: center;
  }
  .card {
    position: relative; overflow: hidden;
    width: var(--card-w); height: var(--card-h);
    box-shadow: 0 6px 14px rgba(0,0,0,0.28);
  }
  .card--red    { --accent: var(--red);    --accent-dark: var(--red-dark);    --accent-light: var(--red-light); }
  .card--orange { --accent: var(--orange); --accent-dark: var(--orange-dark); --accent-light: var(--orange-light); }
  .card--blue   { --accent: var(--blue);   --accent-dark: var(--blue-dark);   --accent-light: var(--blue-light); }

  /* Front side */
  .card-front {
    background: linear-gradient(135deg, var(--card-white) 45%, var(--card-white-shade));
  }
  .card-front .bg-mark {
    position: absolute; right: -30px; top: -40px;
    width: 170px; height: 170px;
    background: var(--mark-grey);
    transform: rotate(0deg);
  }
  .wordmark {
    display: flex; align-items: center; gap: 6px;
    font-weight: 700; letter-spacing: 0.5px; line-height: 1;
  }
  .wordmark .mark-square { width: 12px; height: 12px; background: currentColor; }
  .card-front .wordmark {
    position: absolute; left: 20px; top: 56px;
    font-size: 22px; color: var(--accent);
  }
  .contact {
    position: absolute; left: 20px; top: 96px;
    color: var(--text-grey); font-size: 8.5px; line-height: 1.45;
  }
  .contact .person-name {
    color: var(--accent); font-size: 13px; font-weight: 600; margin-bottom: 3px;
  }
  .accent-bar {
    position: absolute; left: 0; bottom: 14px;
    width: 10px; height: 36px; background: var(--accent);
  }

  /* Back side */
  .card-back {
    background: linear-gradient(150deg, var(--accent-light) 0%, var(--accent) 45%, var(--accent-dark) 100%);
    display: flex; align-items: center; justify-content: center;
  }
  .card-back::before {
    content: ""; position: absolute; left: -20%; top: -60%;
    width: 140%; height: 100%;
    background: linear-gradient(180deg, rgba(255,255,255,0.22), rgba(255,255,255,0));
    transform: rotate(-8deg);
  }
  .card-back .wordmark { position: relative; font-size: 30px; color: #ffffff; }
  .card-back .wordmark .mark-square { width: 16px; height: 16px; }
</style>
</head>
<body>
<main class="card-sheet">
  <section class="card card-front card--red">
    <div class="bg-mark"></div>
    <div class="wordmark"><span class="mark-square"></span>RideHaven</div>
    <div class="contact">
      <p class="person-name">Dale Corvin</p>
      <p>1234 NO ADDRESS</p>
      <p>NO CITY, NO STATE 12345</p>
      <p>dale@ridehavenpowersports.example</p>
      <p>ridehavenpowersports.example</p>
    </div>
    <div class="accent-bar"></div>
  </section>

  <section class="card card-back card--red">
    <div class="wordmark"><span class="mark-square"></span>RideHaven</div>
  </section>

  <section class="card card-front card--blue">
    <div class="bg-mark"></div>
    <div class="wordmark"><span class="mark-square"></span>RideHaven</div>
    <div class="contact">
      <p class="person-name">Dale Corvin</p>
      <p>1234 NO ADDRESS</p>
      <p>NO CITY, NO STATE 12345</p>
      <p>dale@ridehavenpowersports.example</p>
      <p>ridehavenpowersports.example</p>
    </div>
    <div class="accent-bar"></div>
  </section>

  <section class="card card-back card--orange">
    <div class="wordmark"><span class="mark-square"></span>RideHaven</div>
  </section>

  <section class="card card-front card--orange">
    <div class="bg-mark"></div>
    <div class="wordmark"><span class="mark-square"></span>RideHaven</div>
    <div class="contact">
      <p class="person-name">Dale Corvin</p>
      <p>1234 NO ADDRESS</p>
      <p>NO CITY, NO STATE 12345</p>
      <p>dale@ridehavenpowersports.example</p>
      <p>ridehavenpowersports.example</p>
    </div>
    <div class="accent-bar"></div>
  </section>

  <section class="card card-back card--blue">
    <div class="wordmark"><span class="mark-square"></span>RideHaven</div>
  </section>
</main>
</body>
</html>
```